Brindle's Custom Signs and Woodworking Business Card

I run a small business that does custom woodworking and sign making. I have a logo already that I am very fond of, and would like to continue with the theme of the logo. I'd like a business card that adds onto that theme/design and stands out among typical business cards. As you'll be able to see from the logo, we're a patriotic brand and that is paramount to us.
Contact Information for Business Card
beneath the Brindle's logo, I'd like it to say
"Custom Signs & Woodworking"
Also, I'd like the following information template present on the card, preferably with the logos of instagram and facebook present besides the title.
(Name)                                 (Instragram)
(Email)                                  (Facebook)
(Phone)                                 (Website)
I would like for the name, email, and phone number to be editable so that I can have my employees utilize this card design as well. but for my card, my information is as follows
Dan "Brindle" Korvell, CEO                                           @BrindlesCustoms
Dan@BrindlesCustoms.example                                          Brindle's Customs
(555) 274-6103                                                         BrindlesCustoms.example
As for the back side, either a full american flag, or something that catches the eye, designer's preference I suppose.
Font styles to use
Other font styles liked:
- Funkydori, an adobe typekit font. it is the same as used for the logo. I'm not sure how the whole card will look with that, so if it doesn't look right please use something that complements the script style of the logo

```html
<!DOCTYPE html>
<html lang="en">
<head>
<meta charset="utf-8">
<title>Brindle's Custom Signs and Woodworking – Business Card</title>
<link href="https://fonts.googleapis.com/css2?family=Open+Sans:wght@400;700&display=swap" rel="stylesheet">
<style>
  :root {
    --backdrop: #262626;
    --card-white: #ffffff;
    --navy: #2b3572;
    --red: #b3202a;
    --ink: #222222;
    --muted: #555555;
    --sepia-light: #c9bc98;
    --sepia-mid: #8a7e60;
    --sepia-dark: #2e291d;
  }
  * { margin: 0; padding: 0; box-sizing: border-box; }
  html, body {
    width: 899px; height: 1200px; overflow: hidden;
    background: var(--backdrop);
    font-family: "Open Sans", sans-serif;
  }
  .stage {
    width: 899px; height: 1200px;
    display: flex; flex-direction: column;
    align-items: center; justify-content: center; gap: 60px;
  }
  .card {
    position: relative;
    width: 700px; height: 454px;
    overflow: hidden;
    box-shadow: 0 6px 18px rgba(0,0,0,.45);
  }
  /* Front: crew photo */
  .card-front .crew-photo {
    position: absolute; inset: 0;
    background:
      radial-gradient(ellipse at 50% 25%, var(--sepia-light) 0%, var(--sepia-mid) 45%, var(--sepia-dark) 100%);
  }
  .card-front .brand-mark {
    position: absolute; left: 62px; top: 300px;
    font-size: 52px; font-weight: 700;
    color: var(--card-white);
    letter-spacing: .5px;
  }
  /* Back: contact side */
  .card-back { background: var(--card-white); }
  .flag-field {
    position: absolute; left: 0; top: 42px;
    width: 280px; height: 196px;
    background: var(--navy);
  }
  .brand-wordmark {
    position: absolute; left: 346px; top: 92px;
    width: 300px; text-align: center;
    font-size: 58px; font-weight: 700;
    color: var(--navy);
  }
  .contact {
    position: absolute; top: 266px;
    color: var(--muted); font-size: 16px; line-height: 1.6;
  }
  .contact-person { left: 60px; }
  .contact-company { left: 336px; }
  .contact .title {
    color: var(--ink); font-weight: 700; font-size: 19px;
    margin-bottom: 2px;
  }
  .row { display: flex; align-items: center; gap: 7px; margin-top: 2px; }
  .row svg { flex: none; }
  .social-square {
    width: 16px; height: 16px; background: var(--navy); border-radius: 2px;
  }
</style>
</head>
<body>
<main class="stage">
  <section class="card card-front">
    <div class="crew-photo" role="img" aria-label="Sepia group photo of the crew posed with custom motorcycles in front of a painted mural"></div>
    <div class="brand-mark">Brindle's</div>
  </section>

  <section class="card card-back">
    <div class="flag-field" role="img" aria-label="Blue star field of the American flag"></div>
    <div class="brand-wordmark">Brindle's</div>

    <div class="contact contact-person">
      <div class="title">Dan "Brindle" Korvell</div>
      <div>CEO @BrindlesCustoms</div>
      <div class="row">
        <svg width="15" height="15" viewBox="0 0 16 16" aria-hidden="true">
          <circle cx="8" cy="8" r="6.5" fill="none" stroke="var(--red)" stroke-width="2"/>
          <circle cx="8" cy="8" r="2.5" fill="none" stroke="var(--red)" stroke-width="2"/>
        </svg>
        <span>Dan@BrindlesCustoms.example</span>
      </div>
      <div class="row">
        <svg width="15" height="18" viewBox="0 0 12 18" aria-hidden="true">
          <rect x="1" y="1" width="10" height="16" rx="2" fill="none" stroke="var(--red)" stroke-width="1.8"/>
          <circle cx="6" cy="14" r="1" fill="var(--red)"/>
        </svg>
        <span>(555) 274-6103</span>
      </div>
    </div>

    <div class="contact contact-company">
      <div class="title">Custom Signs &amp; Woodworking</div>
      <div>4120 Harlow Ave, Riverside (California)</div>
      <div class="row">
        <svg width="15" height="15" viewBox="0 0 16 16" aria-hidden="true">
          <circle cx="8" cy="8" r="6.5" fill="none" stroke="var(--red)" stroke-width="1.5"/>
          <ellipse cx="8" cy="8" rx="3" ry="6.5" fill="none" stroke="var(--red)" stroke-width="1.2"/>
          <line x1="1.5" y1="8" x2="14.5" y2="8" stroke="var(--red)" stroke-width="1.2"/>
        </svg>
        <span>BrindlesCustoms.example</span>
      </div>
      <div class="row">
        <span class="social-square" aria-hidden="true"></span>
        <span>/BrindlesCustoms</span>
      </div>
    </div>
  </section>
</main>
</body>
</html>
```